Design an A6 flyer for fitness

i am running a 48hr sale and need some flyers designed with the following information on them:

- date of 48 hr. sale is October 29 and 30th
- 3 free personal training sessions
-save $100 joining fee
-first 25 signups will get a gift set
- total savings of over $500
- special rate of $15 per week
*conditions apply

i want the flyer to look classy not tacky and i would like a few options (at least 3 different flyers)

i have attached some photos you can use in the back ground as well as my logo. i have also attached some flyers i have used in the past so you can see the style i like.

```html
<!DOCTYPE html>
<html lang="en">
<head>
<meta charset="utf-8">
<title>Peakform Fitness – 48 Hour Sale Flyer</title>
<link rel="stylesheet" href="https://fonts.googleapis.com/css2?family=Montserrat:wght@500;700;800;900&display=swap">
<style>
  :root {
    --red: #e3261b;
    --black: #111111;
    --ink: #1a1a1a;
    --white: #ffffff;
    --paper: #f7f7f5;
    --stage: #e4e4e4;
    --skin-dark: #3a2418;
    --skin-light: #8a5a3c;
  }
  * { box-sizing: border-box; margin: 0; padding: 0; }
  html, body {
    width: 1200px; height: 646px; overflow: hidden;
    background: var(--stage);
    font-family: "Montserrat", Arial, sans-serif;
  }
  .flyer {
    position: absolute; left: 386px; top: 17px;
    width: 315px; height: 450px;
    transform: scale(1.36); transform-origin: 0 0;
    background: var(--black); overflow: hidden;
    box-shadow: 0 2px 6px rgba(0,0,0,.25);
  }
  .flyer__art { position: absolute; inset: 0; width: 315px; height: 450px; }
  .brand {
    position: absolute; right: 10px; top: 12px;
    display: flex; align-items: center; gap: 6px;
    color: var(--white); font-weight: 800; font-size: 12px; line-height: 1; letter-spacing: .3px;
  }
  .brand__dot { width: 14px; height: 14px; border-radius: 50%; background: var(--white); }
  .sale-date {
    position: absolute; left: 186px; top: 124px; width: 124px;
    color: var(--white); font-weight: 800; font-size: 9.5px; line-height: 1.75; letter-spacing: .2px;
  }
  .sale-date big { font-size: 15px; font-weight: 900; }
  .sale-date sup { font-size: 8px; vertical-align: 3px; }
  .offer {
    position: absolute; left: 72px; top: 238px; width: 220px;
    color: var(--ink);
  }
  .offer__headline { text-align: center; font-weight: 900; font-size: 13.5px; line-height: 1.1; margin-left: -28px; }
  .offer__headline .accent { color: var(--red); display: block; }
  .offer__rule { display: flex; height: 3px; width: 132px; margin: 4px 0 5px 14px; }
  .offer__rule span:first-child { flex: 3; background: var(--black); }
  .offer__rule span:last-child { flex: 1; background: var(--red); }
  .offer__list { list-style: none; font-weight: 500; font-size: 8.6px; line-height: 1.4; }
  .offer__list li::before { content: "- "; }
  .offer__total { color: var(--red); font-weight: 800; font-size: 8.8px; margin-top: 1px; }
  .photo-dot {
    position: absolute; top: 331px; width: 54px; height: 54px; border-radius: 50%;
    border: 2px solid var(--black);
  }
  .photo-dot--swim { left: 25px; background: radial-gradient(circle at 40% 45%, #7fc6e6, #2c7fb0); }
  .photo-dot--class { left: 113px; background: linear-gradient(#c9c7c2, #6e6862); }
  .photo-dot--tennis { left: 226px; background: radial-gradient(circle at 55% 40%, #c4e23c, #1e3c6e 70%); }
  .conditions {
    position: absolute; left: 0; right: 0; top: 393px; text-align: center;
    font-weight: 800; font-size: 8.5px; color: var(--ink);
  }
  .conditions::before, .conditions::after {
    content: ""; display: inline-block; width: 6px; height: 6px; border-radius: 50%;
    background: var(--red); margin: 0 4px; vertical-align: 1px;
  }
  .map-spot {
    position: absolute; left: 8px; top: 404px; width: 34px; height: 30px;
    background: linear-gradient(135deg, #e9e6dc, #cfd8c4); border: 1px solid #bbb;
  }
  .address {
    position: absolute; left: 48px; top: 405px;
    font-size: 7.4px; font-weight: 500; line-height: 1.3; color: var(--ink);
  }
  .contact {
    position: absolute; right: 8px; top: 405px; text-align: right;
    font-size: 7.4px; font-weight: 500; line-height: 1.9; color: var(--ink);
  }
  .contact svg { width: 7px; height: 7px; margin-left: 5px; vertical-align: -1px; }
</style>
</head>
<body>
<main class="flyer">
  <svg class="flyer__art" viewBox="0 0 315 450" aria-hidden="false">
    <defs>
      <linearGradient id="athlete" x1="0" y1="0" x2="1" y2="1">
        <stop offset="0" stop-color="#1d1412"/>
        <stop offset=".45" stop-color="var(--skin-light)"/>
        <stop offset="1" stop-color="var(--skin-dark)"/>
      </linearGradient>
    </defs>
    <rect class="athlete-photo" x="0" y="0" width="200" height="320" fill="url(#athlete)" role="img" aria-label="Photo of an athlete lifting a red dumbbell"/>
    <polygon class="top-stripe" points="135,0 150,0 315,110 315,122" fill="var(--red)"/>
    <polygon class="top-stripe" points="170,0 200,0 315,78 315,98" fill="var(--red)"/>
    <polygon class="date-panel" points="180,100 315,70 315,300 145,182" fill="var(--red)"/>
    <polygon class="chevron chevron--black" points="0,290 145,156 315,272 315,284 145,168 0,302" fill="var(--black)"/>
    <polygon class="chevron chevron--white" points="0,302 145,168 315,284 315,289 145,173 0,307" fill="var(--white)"/>
    <polygon class="chevron chevron--red" points="0,307 145,173 315,289 315,297 145,181 0,315" fill="var(--red)"/>
    <polygon class="offer-panel" points="0,320 145,188 315,303 315,450 0,450" fill="var(--paper)"/>
  </svg>

  <div class="brand"><span class="brand__dot"></span>PEAKFORM<br>FITNESS</div>

  <p class="sale-date">DATE OF <big>48</big> HR<br>SALE IS OCTOBER<br><big>29</big><sup>th</sup> AND <big>30</big><sup>th</sup></p>

  <section class="offer">
    <h1 class="offer__headline">SAVE $100<span class="accent">JOINING FEE</span></h1>
    <div class="offer__rule"><span></span><span></span></div>
    <ul class="offer__list">
      <li>special rate of $15 per week</li>
      <li>first 25 signups will get a gift set</li>
      <li>3 free personal training sessions</li>
    </ul>
    <p class="offer__total">TOTAL SAVING OF OVER $500</p>
  </section>

  <div class="photo-dot photo-dot--swim" role="img" aria-label="Photo of a swimmer in a pool"></div>
  <div class="photo-dot photo-dot--class" role="img" aria-label="Photo of a group fitness class"></div>
  <div class="photo-dot photo-dot--tennis" role="img" aria-label="Photo of a tennis ball and racket"></div>

  <p class="conditions">CONDITIONS APPLY</p>

  <div class="map-spot" role="img" aria-label="Small street map showing the gym location"></div>
  <p class="address">14 Harlow St<br>Eastbrook<br>N S W &nbsp;2150</p>
  <p class="contact">
    0400 123 987<svg viewBox="0 0 10 10"><path d="M2 1l2 0 1 2.5-1.3 1a6 6 0 0 0 2.8 2.8l1-1.3L10 7v2c0 .6-.5 1-1 1A9 9 0 0 1 0 1c0-.5.4-1 1-1z" fill="var(--ink)"/></svg><br>
    info@peakformfitness.com.au<svg viewBox="0 0 10 10"><circle cx="5" cy="5" r="4.5" fill="var(--ink)"/><path d="M.5 5h9M5 .5c-2.5 2.5-2.5 6.5 0 9M5 .5c2.5 2.5 2.5 6.5 0 9" stroke="var(--white)" stroke-width=".8" fill="none"/></svg>
  </p>
</main>
</body>
</html>
```